Design NEW business card

We would like a business card using the colour deep red wine or dark navy blue textured background (patterned or not, open to suggestions) with a high gloss debossed rose gold/copper TM Thomas Marlow Jewellery business name (Provided). I have included images for your review we would like to keep our currently logo and business name on the front but you can change the layout and positioning. For the back of the card we are open to all suggestions/variations.
Use our current TM Thomas Marlow Jewellery logo (Provided image)

```html
<!DOCTYPE html>
<html lang="en">
<head>
<meta charset="utf-8">
<title>Thomas Marlow Jewellery – Business Cards</title>
<link rel="stylesheet" href="https://fonts.googleapis.com/css2?family=Montserrat:wght@300;400&display=swap">
<style>
  :root {
    --backdrop: #e4e4e3;
    --wine: #5a232a;
    --rose-gold: #c99a7b;
    --ivory: #f3e9e6;
  }
  * { margin: 0; padding: 0; box-sizing: border-box; }
  html, body {
    width: 1200px;
    height: 960px;
    overflow: hidden;
    background: var(--backdrop);
    font-family: "Montserrat", Arial, sans-serif;
  }
  .canvas {
    position: relative;
    width: 1200px;
    height: 960px;
  }
  .card {
    position: absolute;
    width: 600px;
    height: 343px;
    background: var(--wine);
  }
  .card--contact { left: 314px; top: 113px; }
  .card--brand { left: 311px; top: 472px; }

  /* Contact side */
  .contact-monogram {
    position: absolute;
    left: 0; right: 0;
    top: 180px;
    transform: translateY(-100%);
    text-align: center;
    color: var(--rose-gold);
    font-weight: 300;
    font-size: 52px;
    letter-spacing: 0.06em;
    line-height: 1;
    top: 150px;
  }
  .contact-name {
    position: absolute;
    left: 0; right: 0; top: 175px;
    text-align: center;
    color: var(--rose-gold);
    font-weight: 400;
    font-size: 19px;
    letter-spacing: 0.02em;
  }
  .contact-role {
    position: absolute;
    left: 0; right: 0; top: 201px;
    text-align: center;
    color: var(--ivory);
    font-weight: 400;
    font-size: 13px;
    letter-spacing: 0.03em;
  }
  .contact-details {
    position: absolute;
    left: 0; right: 0; top: 227px;
    text-align: center;
    color: var(--ivory);
    font-weight: 400;
    font-size: 14.5px;
    line-height: 19.5px;
    letter-spacing: 0.02em;
    list-style: none;
  }
  .contact-details .divider { margin: 0 6px; }

  /* Brand side */
  .brand-name {
    position: absolute;
    left: 0; right: 0; top: 62px;
    text-align: center;
    color: var(--rose-gold);
    font-weight: 300;
  }
  .brand-name__initials {
    display: block;
    font-size: 96px;
    line-height: 1;
    letter-spacing: 0.04em;
  }
  .brand-name__house {
    display: block;
    margin-top: 34px;
    font-size: 26px;
    letter-spacing: 0.2em;
    padding-left: 0.2em;
  }
  .brand-name__trade {
    display: block;
    margin-top: 10px;
    font-size: 10px;
    letter-spacing: 1.05em;
    padding-left: 1.05em;
  }
</style>
</head>
<body>
<main class="canvas">
  <section class="card card--contact" aria-label="Business card, contact side">
    <p class="contact-monogram">TM</p>
    <h1 class="contact-name">DANIEL HART</h1>
    <p class="contact-role">CEO/FOUNDER</p>
    <ul class="contact-details">
      <li>2914 Willowbrook Lane, Fairbanks, Alaska 99701</li>
      <li>555 214 7690<span class="divider">|</span>hello@thomasmarlow.com</li>
      <li>www.thomasmarlow.com</li>
    </ul>
  </section>

  <section class="card card--brand" aria-label="Business card, brand side">
    <h2 class="brand-name">
      <span class="brand-name__initials">TM</span>
      <span class="brand-name__house">THOMAS MARLOW</span>
      <span class="brand-name__trade">JEWELLERY</span>
    </h2>
  </section>
</main>
</body>
</html>
```